Telecommunications/Power civil contractor needs business card design

Were a new telecommunications/power underground civil contractor that is looking for a new business card design. Our company colours are silver or grey and orange. Feel free to use the white background logo or the black background logo.

Target Market(s)

Local contractors, utility companies, private sector mining/energy companies, developers.

Industry/Entity Type

Telecommunications

Contact Information for Business Card

Each card will need the following info:
Persons name:
Title:
E-mail:
Phone number:
Shop Address:
Mailing Address:

Requirements
Must have
• Each card will need the following info:
• Persons name:
• Title:
• E-mail:
• Phone number:
• Shop Address:
• Mailing Address:

```html
<!DOCTYPE html>
<html lang="en">
<head>
<meta charset="utf-8">
<title>Trenchway Contracting Inc – Business Card</title>
<link rel="stylesheet" href="https://fonts.googleapis.com/css2?family=Source+Sans+3:wght@400;600;700&display=swap">
<style>
  :root {
    --orange: #f15a24;
    --grey: #6d6e71;
    --ink: #231f20;
    --white: #ffffff;
    --backdrop: #e9e7e4;
  }
  * { margin: 0; padding: 0; box-sizing: border-box; }
  html, body { width: 1200px; height: 900px; overflow: hidden; }
  body {
    background: var(--backdrop);
    font-family: "Source Sans 3", sans-serif;
    position: relative;
  }
  .card {
    position: absolute;
    border-radius: 14px;
    overflow: hidden;
    box-shadow: 0 4px 14px rgba(0,0,0,0.12);
  }
  .card-front {
    left: 78px; top: 34px; width: 588px; height: 364px;
    background: var(--white);
  }
  .card-back {
    left: 389px; top: 506px; width: 566px; height: 350px;
    background: var(--orange);
  }
  .band { position: absolute; left: 0; right: 0; }
  .card-front .band { top: 90px; height: 98px; background: var(--orange); }
  .card-back .band { top: 42px; height: 95px; background: var(--white); }
  .mark { position: absolute; border-radius: 50%; }
  .card-front .mark {
    left: 224px; top: 86px; width: 112px; height: 112px;
    background: var(--white);
  }
  .card-back .mark {
    left: 229px; top: 32px; width: 116px; height: 116px;
    background: var(--orange);
  }
  .identity {
    position: absolute; top: 30px; left: 0; right: 0;
    text-align: center; font-size: 21px; line-height: 1;
  }
  .identity .first { color: var(--orange); font-weight: 600; }
  .identity .last { color: var(--grey); font-weight: 600; }
  .identity .divider { color: var(--ink); margin: 0 6px; }
  .identity .title { color: var(--ink); font-size: 16px; }
  .company {
    position: absolute; left: 0; right: 0;
    text-align: center; font-weight: 700; line-height: 1;
    text-transform: uppercase; letter-spacing: 1px;
  }
  .card-front .company { top: 222px; color: var(--grey); }
  .card-back .company { top: 168px; color: var(--white); }
  .company .name { display: block; font-size: 32px; }
  .company .suffix { display: block; font-size: 17px; margin-top: 2px; letter-spacing: 1.5px; }
  .contact {
    position: absolute; top: 308px; left: 0; right: 0;
    text-align: center; font-size: 16px; color: var(--ink);
  }
  .contact .divider { margin: 0 6px; }
  .addresses {
    position: absolute; top: 232px; left: 0; right: 0;
    text-align: center; color: var(--white);
  }
  .address { margin-bottom: 14px; line-height: 1.15; }
  .address .label { display: block; font-size: 19px; font-weight: 600; }
  .address .line { display: block; font-size: 15.5px; }
</style>
</head>
<body>
  <section class="card card-front" aria-label="Card front">
    <p class="identity">
      <span class="first">Marcus</span> <span class="last">Hale</span><span class="divider">|</span><span class="title">Managing Director</span>
    </p>
    <div class="band"></div>
    <div class="mark"></div>
    <p class="company"><span class="name">Trenchway</span><span class="suffix">Contracting Inc</span></p>
    <p class="contact">(044)-555-0182<span class="divider">|</span>info@trenchway.example</p>
  </section>

  <section class="card card-back" aria-label="Card back">
    <div class="band"></div>
    <div class="mark"></div>
    <p class="company"><span class="name">Trenchway</span><span class="suffix">Contracting Inc</span></p>
    <div class="addresses">
      <p class="address"><span class="label">Mailing Address</span><span class="line">12345, Address Goes Here Country Name, 123456</span></p>
      <p class="address"><span class="label">Shop Address</span><span class="line">12345, Address Goes Here Country Name, 123456</span></p>
    </div>
  </section>
</body>
</html>
```